Larkmoor Business Card Design Project

Double side card , just the logo on oxford white background on one side , and the rest of the information on the other side..
the company name is : Larkmoor Continental General Trading LLC.
logo is already attached
the card to show in the info side: company name, employee name and position (job title) phone number, fax number, email address, P.O. box, Location (city and country)
deadline is already extended 4 all to have more time... thanks

```html
<!DOCTYPE html>
<html lang="en">
<head>
<meta charset="utf-8">
<title>Larkmoor Continental General Trading LLC – Business Card</title>
<link rel="stylesheet" href="https://fonts.googleapis.com/css2?family=Crimson+Text:ital,wght@0,400;0,700;1,700&display=swap">
<style>
  :root {
    --sky-top: #36b6e8;
    --sky-bottom: #0a3bdc;
    --paper: #fdfdfd;
    --white: #ffffff;
    --ink-blue: #2b4fd2;
  }
  html, body {
    margin: 0;
    padding: 0;
    overflow: hidden;
    background: var(--paper);
  }
  .card {
    position: relative;
    width: 1200px;
    height: 702px;
    overflow: hidden;
    background: linear-gradient(180deg, var(--sky-top) 0%, var(--sky-bottom) 68%);
    font-family: "Crimson Text", "Times New Roman", serif;
  }
  .card__wave {
    position: absolute;
    inset: 0;
    width: 1200px;
    height: 702px;
  }
  .card__wave path { fill: var(--paper); }
  .brand-mark {
    position: absolute;
    top: 78px;
    left: 0;
    width: 1200px;
    text-align: center;
    color: var(--white);
    font-size: 34px;
    font-weight: 700;
    line-height: 1;
  }
  .company-name {
    position: absolute;
    top: 186px;
    left: 0;
    width: 1200px;
    margin: 0;
    text-align: center;
    color: var(--white);
    font-size: 62px;
    font-weight: 700;
    line-height: 58px;
  }
  .company-rule {
    position: absolute;
    top: 323px;
    left: 249px;
    width: 761px;
    height: 9px;
    background: var(--white);
  }
  .employee {
    position: absolute;
    top: 354px;
    left: 0;
    width: 1200px;
    text-align: center;
    color: var(--white);
  }
  .employee__name {
    display: block;
    font-size: 33px;
    font-weight: 700;
    font-style: italic;
    line-height: 34px;
  }
  .employee__title {
    display: block;
    font-size: 25px;
    font-weight: 400;
    line-height: 25px;
  }
  .contact {
    position: absolute;
    margin: 0;
    color: var(--ink-blue);
    font-size: 29px;
    font-weight: 400;
    line-height: 33px;
    font-style: normal;
  }
  .contact--left { top: 520px; left: 112px; text-align: left; }
  .contact--right { top: 550px; right: 107px; text-align: right; }
</style>
</head>
<body>
  <main class="card">
    <svg class="card__wave" viewBox="0 0 1200 702" aria-hidden="true">
      <path d="M0,455 C110,436 210,428 300,448 C480,492 880,500 1200,552 L1200,702 L0,702 Z"/>
    </svg>

    <div class="brand-mark">Larkmoor</div>

    <h1 class="company-name">Larkmoor Continental<br>General Trading LLC</h1>
    <div class="company-rule"></div>

    <div class="employee">
      <span class="employee__name">JOHN DOE SMITH</span>
      <span class="employee__title">Job Title Senior Editor</span>
    </div>

    <address class="contact contact--left">
      Sample phone number<br>
      Sample Fax Number<br>
      sample.email@larkmoormail.com
    </address>

    <address class="contact contact--right">
      Sample P.O. box,<br>
      Location (city and country)
    </address>
  </main>
</body>
</html>
```